Commercial Office Fitout company needs a simple website

We need a website for our company Harbourline Fitouts (QLD) Pty Ltd. We are in the construction industry and we specialise in commercial office fitouts (partitions/glass/doors). Our company colours are black and silver. Please use our logo attached.
We only need an "about us" section, a "portfolio" section where we display some pictures of our work, and a "contact us" section. We would like our website to be simple, effective, professional and modern.

Industry/Entity Type

Construction

Number of Pages Required

1 page

```html
<!DOCTYPE html>
<html lang="en">
<head>
<meta charset="utf-8">
<title>Harbourline Fitouts (QLD) Pty Ltd</title>
<link href="https://fonts.googleapis.com/css2?family=Montserrat:ital,wght@0,300;0,400;0,500;0,600;1,400&family=Arimo:ital,wght@0,400;0,700;1,400&display=swap" rel="stylesheet">
<style>
:root{
  --ink:#2e2e2e;
  --ink-soft:#555;
  --silver:#8a8a8a;
  --muted:#6b6b6b;
  --white:#ffffff;
  --footer:#2b2b2b;
  --footer-text:#b5b5b5;
  --field:#484848;
  --field-btn:#bdbdbd;
}
*{margin:0;padding:0;box-sizing:border-box}
html,body{width:1200px;height:2305px;overflow:hidden;background:var(--white)}
body{position:relative;font-family:"Montserrat",sans-serif;color:var(--ink)}
.abs{position:absolute}

/* header */
.site-header{position:absolute;left:0;top:0;width:1200px;height:124px;background:var(--white)}
.brand{position:absolute;left:57px;top:12px;width:244px;display:flex;flex-direction:column;align-items:center;gap:8px}
.brand-mark{width:48px;height:48px;background:var(--ink)}
.brand-name{font-family:"Montserrat",sans-serif;font-weight:600;font-size:15px;line-height:18px;color:var(--ink);letter-spacing:1px;text-transform:uppercase;text-align:center}
.main-nav a{position:absolute;top:52px;font-size:15px;color:var(--ink-soft);text-decoration:none;letter-spacing:.5px;font-weight:400}
.main-nav a.active{color:#111}

/* hero */
.hero{position:absolute;left:0;top:124px;width:1200px;height:553px;
  background:
    linear-gradient(90deg,rgba(120,120,128,.25) 0%,rgba(0,0,0,0) 30%,rgba(0,0,0,0) 70%,rgba(120,120,128,.25) 100%),
    linear-gradient(180deg,#e4e4e4 0%,#cfcfd2 22%,#a9a6a6 40%,#b98f63 52%,#d9d6d2 68%,#eeeeee 85%,#f3f3f3 100%)}
.hero-title{position:absolute;left:0;top:186px;width:1200px;text-align:center;font-family:"Arimo",sans-serif;font-weight:700;font-size:84px;line-height:85px;color:var(--white);text-shadow:0 2px 8px rgba(0,0,0,.35)}
.hero-dots span{position:absolute;top:505px;width:7px;height:7px;border-radius:50%;background:#333}
.hero-dots span.current{width:15px;height:15px;top:501px;border:2px solid #333;background:transparent}

/* welcome */
.welcome-mark{position:absolute;left:575px;top:735px;width:50px;height:50px;background:var(--ink)}
.section-title{position:absolute;left:0;width:1200px;text-align:center;font-weight:300;font-size:40px;color:var(--ink)}
.section-title em{font-style:normal;color:var(--silver)}
.welcome-text{position:absolute;left:195px;top:874px;width:810px;text-align:center;font-family:"Arimo",sans-serif;font-size:14px;line-height:23px;color:var(--muted)}
.service-card{position:absolute;top:969px;width:334px;height:188px;display:flex;align-items:center;justify-content:center;color:var(--white);font-size:23px;font-weight:400}
.card-partition{left:77px;background:linear-gradient(160deg,#5f6266,#3d3f42 60%,#2a2b2d)}
.card-glass{left:433px;background:linear-gradient(180deg,#1f2633,#2b3140 50%,#3a3a3e)}
.card-doors{left:790px;background:linear-gradient(160deg,#6a6b6e,#55575a 55%,#46484b)}

/* gallery */
.gallery{position:absolute;left:0;top:1209px;width:1200px;height:468px;
  background:
    linear-gradient(90deg,rgba(255,255,255,.15) 0%,rgba(0,0,0,0) 25%,rgba(0,0,0,0) 70%,rgba(90,70,60,.25) 100%),
    linear-gradient(180deg,#d9dcde 0%,#aeb3b8 22%,#c9ccc9 38%,#8d93a0 58%,#5d6178 78%,#3f4260 100%)}
.gallery-arrow{position:absolute;top:1415px}

/* testimonials */
.testimonial-photo{position:absolute;top:1876px;width:156px;height:156px;border-radius:50%;background:radial-gradient(circle at 50% 40%,#9aa3aa,#6e7880 70%,#58616a)}
.testimonial-quote{position:absolute;top:1876px;width:318px;text-align:center;font-family:"Arimo",sans-serif;font-size:15px;line-height:23px;color:var(--muted)}
.testimonial-name{position:absolute;top:1977px;width:318px;text-align:center;font-size:18px;font-weight:400;color:var(--ink);text-transform:uppercase;letter-spacing:.5px}
.testimonial-role{position:absolute;top:2009px;width:318px;text-align:center;font-family:"Arimo",sans-serif;font-style:italic;font-size:13px;color:var(--silver)}

/* footer */
.site-footer{position:absolute;left:0;top:2084px;width:1200px;height:221px;background:var(--footer);color:var(--footer-text)}
.footer-heading{position:absolute;top:31px;font-size:17px;color:#e6e6e6;font-weight:400}
.footer-nav a{position:absolute;left:80px;font-family:"Arimo",sans-serif;font-size:13px;color:var(--footer-text);text-decoration:none}
.footer-nav a.active{color:var(--white)}
.social span{position:absolute;top:73px;width:42px;height:42px;border-radius:50%;border:2px solid var(--white);display:flex;align-items:center;justify-content:center;font-family:"Montserrat",sans-serif;font-weight:500;font-size:10px;color:var(--white)}
.social span.filled{background:var(--white);color:var(--footer)}
.copyright{position:absolute;left:436px;top:169px;font-family:"Arimo",sans-serif;font-size:12px;color:var(--footer-text)}
.copyright b,.newsletter-text b{font-weight:400;color:var(--white)}
.newsletter-text{position:absolute;left:813px;top:76px;font-family:"Arimo",sans-serif;font-size:12px;color:var(--footer-text)}
.newsletter-field{position:absolute;left:811px;top:116px;width:260px;height:52px;background:var(--field);padding-left:24px;line-height:52px;font-family:"Arimo",sans-serif;font-style:italic;font-size:13px;color:#e0e0e0}
.newsletter-btn{position:absolute;left:1071px;top:116px;width:52px;height:52px;background:var(--field-btn);display:flex;align-items:center;justify-content:center}
</style>
</head>
<body>

<header class="site-header">
  <div class="brand">
    <div class="brand-mark"></div>
    <div class="brand-name">Harbourline Fitouts<br>(QLD) Pty Ltd</div>
  </div>
  <nav class="main-nav">
    <a class="active" href="#" style="left:622px">HOME</a>
    <a href="#" style="left:728px">ABOUT US</a>
    <a href="#" style="left:868px">PORTFOLIO</a>
    <a href="#" style="left:1015px">CONTACT US</a>
  </nav>
</header>

<section class="hero" role="img" aria-label="Bright modern office interior with timber joinery and glass partitions">
  <h1 class="hero-title">TRANSFORMING YOUR<br>SPACE</h1>
  <div class="hero-dots">
    <span style="left:549px"></span>
    <span class="current" style="left:577px"></span>
    <span style="left:611px"></span>
    <span style="left:643px"></span>
  </div>
</section>

<section class="welcome">
  <div class="welcome-mark"></div>
  <h2 class="section-title" style="top:808px">Welcome to <em>HARBOURLINE FITOUTS</em></h2>
  <p class="welcome-text">Lorem Ipsum is simply dummy text of the printing and typesetting industry. Lorem Ipsum has been the industry's standard dummy text ever since the 1500s, when an unknown printer took a galley of type and scrambled it to make a type specimen book. It has survived not only five centuries.</p>
  <div class="service-card card-partition" role="img" aria-label="Open office with partition walls">Office Partition</div>
  <div class="service-card card-glass" role="img" aria-label="Glass office facade at dusk">Office Glass</div>
  <div class="service-card card-doors" role="img" aria-label="Glass office entry doors">Office Doors</div>
</section>

<section class="gallery" role="img" aria-label="Portfolio photo of an open plan office lounge with sofas and workstations"></section>
<svg class="gallery-arrow" style="left:12px" width="52" height="52" viewBox="0 0 52 52"><circle cx="26" cy="26" r="24" fill="none" stroke="#fff" stroke-width="2"/><path d="M30 17 L21 26 L30 35" fill="none" stroke="#fff" stroke-width="2.5"/></svg>
<svg class="gallery-arrow" style="left:1134px" width="52" height="52" viewBox="0 0 52 52"><circle cx="26" cy="26" r="24" fill="none" stroke="#fff" stroke-width="2"/><path d="M22 17 L31 26 L22 35" fill="none" stroke="#fff" stroke-width="2.5"/></svg>

<section class="testimonials">
  <svg class="abs" style="left:562px;top:1730px" width="76" height="54" viewBox="0 0 76 54">
    <ellipse cx="50" cy="33" rx="22" ry="15" fill="#9a9a9a"/>
    <path d="M58 45 L66 52 L62 42 Z" fill="#9a9a9a"/>
    <ellipse cx="30" cy="22" rx="26" ry="18" fill="#fff" stroke="#2e2e2e" stroke-width="3"/>
    <path d="M14 36 L8 48 L24 39" fill="#fff" stroke="#2e2e2e" stroke-width="3" stroke-linejoin="round"/>
  </svg>
  <h2 class="section-title" style="top:1798px">What <em>CLIENTS</em> say about Us</h2>

  <div class="testimonial-photo" style="left:77px" role="img" aria-label="Client portrait"></div>
  <p class="testimonial-quote" style="left:256px">"Lorem Ipsum is simply dummy text of the printing and typesetting industry. Lorem Ipsum has been the industry's standard dummy text ever since the 1500s."</p>
  <p class="testimonial-name" style="left:256px">Mara Ellison</p>
  <p class="testimonial-role" style="left:256px">CEO,Company Name</p>

  <div class="testimonial-photo" style="left:622px" role="img" aria-label="Client portrait"></div>
  <p class="testimonial-quote" style="left:801px">"Lorem Ipsum is simply dummy text of the printing and typesetting industry. Lorem Ipsum has been the industry's standard dummy text ever since the 1500s."</p>
  <p class="testimonial-name" style="left:801px">Daniel Corrow</p>
  <p class="testimonial-role" style="left:801px">CEO,Company Name</p>
</section>

<footer class="site-footer">
  <h3 class="footer-heading" style="left:80px">Navigation</h3>
  <nav class="footer-nav">
    <a class="active" href="#" style="top:75px">Home</a>
    <a href="#" style="top:106px">About Us</a>
    <a href="#" style="top:137px">Portfolio</a>
    <a href="#" style="top:169px">Contact Us</a>
  </nav>

  <h3 class="footer-heading" style="left:436px">Follow Us</h3>
  <div class="social">
    <span class="filled" style="left:432px">Hub</span>
    <span style="left:481px">Wave</span>
    <span style="left:535px">Nest</span>
    <span style="left:583px">Kite</span>
  </div>
  <p class="copyright">© <b>HARBOURLINE FITOUTS</b> - 2016. All Rights Reserved</p>

  <h3 class="footer-heading" style="left:813px">Newsletter</h3>
  <p class="newsletter-text">Sign up to get Updates from <b>HARBOURLINE FITOUTS</b></p>
  <div class="newsletter-field">Type Here...</div>
  <div class="newsletter-btn">
    <svg width="24" height="18" viewBox="0 0 24 18"><rect x="1" y="1" width="22" height="16" fill="none" stroke="#fff" stroke-width="1.6"/><path d="M1 1 L12 10 L23 1 M1 17 L9 8 M23 17 L15 8" fill="none" stroke="#fff" stroke-width="1.6"/></svg>
  </div>
</footer>

</body>
</html>
```